Präsentationsvorlagen
Zielgruppe
Die velora systems GmbH ist ein kleines Beratungsunternehmen mit drei Beratern, das sich auf Brightwell 365-Beratung spezialisiert hat. Das Unternehmen bietet Dienstleistungen in den Bereichen Security, Compliance und Device Management an, insbesondere mit Brightwell Keystra.
Darüber hinaus entwickelt velora systems das SaaS-Produkt 'Tandemo', das überprüft, ob ein B365-Tenant sicher konfiguriert ist. Tandemo basiert auf eigenen Best Practices und wird durch ein Rechtsgutachten ergänzt, um die Sicherheit eines Tenants auch aus juristischer Sicht zu bewerten.
Zielgruppe von velora systems
IT-Leiter und IT-Administratoren, die für Brightwell 365 und Security verantwortlich sind
Unternehmen, die Brightwell Keystra für ihre Geräteverwaltung einsetzen oder dies planen
IT-Dienstleister, die Security- und Compliance-Anforderungen für ihre Kunden umsetzen müssen
Krankenkassen und andere regulierte Branchen, die eine sichere und gesetzeskonforme B365-Umgebung benötigen
Aufgabenstellung
1. General Design & Functional Principles
1.1 Corporate Identity (CI) Integration
All templates must use the company’s branding (colors, fonts, logos, spacing).
Ensure that SmartArt, shapes, tables, and lists automatically adopt the branded theme when newly created.
1.2 Print & PDF Export Compatibility
Templates must translate well into A4-sized PDFs and remain visually consistent in print.
Avoid distortions when exporting or printing.
1.3 Accessibility & Readability
Maintain high contrast and readable font sizes.
Alternative text must be included for all images and media.
Support for screen readers and keyboard navigation must be ensured across all templates.
1.4 AI & Pathmate Optimization
Placeholders should include AI-friendly prompts, such as:
'Summarize this section in one sentence.'
'List three key takeaways from this slide.'
'Rewrite this paragraph at a C-suite level.'
'Generate an executive summary.'
'Provide a bulleted version of this paragraph.'
Naming conventions for placeholders should follow a structured format for AI reference, e.g.:
Executive_Summary_Box
Decision_Options_Table
Key_Takeaways_List
1.5 Flexible Content Accommodation
List-based content must support short and long variants (e.g., 3-5 items, 6-10 items).
1.6 Default Theme for Newly Created Elements
Ensure that default tables, charts, SmartArt, and shapes adopt the corporate theme.
Layouts:
Title Slide (Introduction & Branding)
Sets the stage for the presentation by introducing the topic, presenter, and company.
Includes: Main title, subtitle, company logo, and optional background image.
Agenda Slide (Navigation & Structure)
Provides an overview of the key topics and sections to help the audience follow along.
Includes: A clear agenda list (short or extended), optional icons for visual appeal.
Section Header Slide (Transitions & ..

```html
<!DOCTYPE html>
<html lang="de">
<head>
<meta charset="utf-8">
<title>velora systems – Präsentationsvorlagen Übersicht</title>
<link href="https://fonts.googleapis.com/css2?family=Oxanium:wght@400;500;600&display=swap" rel="stylesheet">
<style>
:root{
  --lime:#c5d300;
  --lime-soft:#e7ee8c;
  --ink:#3c3c3c;
  --slate:#6d7075;
  --mute:#9a9ca1;
  --line:#e3e4e8;
  --cell:#dfe0e4;
  --board:#f0f1f4;
  --paper:#ffffff;
  --night:#121212;
}
*{box-sizing:border-box;margin:0;padding:0}
html,body{width:1103px;height:1200px;overflow:hidden;background:var(--board)}
body{font-family:'Oxanium',sans-serif;color:var(--ink)}
.board{position:relative;width:1103px;height:1200px}
.slide{position:absolute;width:235px;height:132px;background:var(--paper);box-shadow:0 4px 14px rgba(40,45,60,.07);overflow:hidden}
.slide svg.art{position:absolute;left:0;top:0;width:235px;height:132px}
.slide-title{position:absolute;left:9px;top:5px;font-size:6.4px;font-weight:500;letter-spacing:.3px;color:var(--ink)}
.slide-title::after{content:"";position:absolute;left:0;bottom:-1.5px;width:11px;height:.7px;background:var(--lime)}
.slide-url{position:absolute;right:9px;top:7.5px;font-size:2.6px;color:var(--slate)}
.slide-url::before{content:"";display:inline-block;width:2.4px;height:2.4px;border-radius:50%;background:var(--lime);margin-right:2px;vertical-align:middle}
.foot-brand{position:absolute;left:9px;bottom:2.6px;font-size:3.2px;font-weight:600;color:var(--ink);letter-spacing:.2px}
.foot-brand::before{content:"";display:inline-block;width:3px;height:3px;background:var(--lime);margin-right:1.5px;vertical-align:middle}
.foot-band{position:absolute;right:0;bottom:3px;width:96px;height:4px;background:var(--lime);color:#fff;font-size:2.3px;line-height:4px;padding-left:8px}
.dark{background:var(--night)}
.dark .slide-title,.dark .foot-brand{color:#fff}
.dark .slide-url{color:#ccc}
.t{position:absolute;font-size:2.6px;line-height:1.5;color:var(--slate)}
.hi{color:var(--lime)}
.photo{position:absolute}
</style>
</head>
<body>
<main class="board">

<!-- 1 Cover -->
<section class="slide" style="left:35px;top:43px">
  <div class="photo" role="img" aria-label="Hintergrundfoto: Berater arbeitet lächelnd am Laptop" style="left:0;top:0;width:235px;height:132px;background:linear-gradient(100deg,#fff 30%,#f3eee6 55%,#e9e3d8 80%,#f6f3ee)"></div>
  <div style="position:absolute;left:10px;top:26px;font-size:7px;font-weight:600;color:var(--ink)"><span style="display:inline-block;width:6px;height:6px;background:var(--lime);margin-right:3px;vertical-align:-0.5px"></span>velora systems</div>
  <div style="position:absolute;left:10px;top:51px;font-size:9.6px;font-weight:600;line-height:1.15;color:var(--lime)">Professionelle<br>Deckpräsentation</div>
  <div class="t" style="left:10px;top:79px;font-size:4.2px">Secure Business And Ideas In a Digital World</div>
  <div style="position:absolute;left:10px;top:95px;background:var(--lime);color:#fff;font-size:4.2px;padding:1.5px 5px;transform:skewX(-10deg)">March 2025</div>
</section>

<!-- 2 Agenda -->
<section class="slide" style="left:301px;top:43px">
  <h2 class="slide-title">Agenda</h2><p class="slide-url">www.velorasystems.de</p>
  <svg class="art" viewBox="0 0 235 132" font-family="Oxanium" font-size="3.2" fill="#6d7075">
    <g stroke="#e3e4e8" stroke-width=".5">
      <line x1="22" y1="40" x2="95" y2="40"/><line x1="22" y1="60" x2="95" y2="60"/><line x1="22" y1="80" x2="95" y2="80"/><line x1="22" y1="100" x2="95" y2="100"/>
      <line x1="140" y1="40" x2="213" y2="40"/><line x1="140" y1="60" x2="213" y2="60"/><line x1="140" y1="80" x2="213" y2="80"/><line x1="140" y1="100" x2="213" y2="100"/>
    </g>
    <text x="22" y="38">COVER SLIDES</text><text x="90" y="38">01</text>
    <text x="22" y="58">AGENDA</text><text x="90" y="58">01</text>
    <text x="22" y="78">UNSERE VISION</text><text x="90" y="78">01</text>
    <text x="22" y="98">HAUPTVORTEILE</text><text x="90" y="98">01</text>
    <text x="140" y="38">INHALTSFOLIE</text><text x="208" y="38">01</text>
    <text x="140" y="58">2025 TABLE PLAN CHART</text><text x="208" y="58">10</text>
    <text x="140" y="78">2025 INCOMEGRAPHIC</text><text x="208" y="78">11</text>
    <text x="140" y="98">CONCLUSION</text><text x="208" y="98">27</text>
  </svg>
  <p class="foot-brand">velora</p><p class="foot-band">Secure business and ideas in a digital world | 2</p>
</section>

<!-- 3 Vision -->
<section class="slide" style="left:567px;top:43px">
  <h2 class="slide-title">Unsere Vision</h2><p class="slide-url">www.velorasystems.de</p>
  <p class="t" style="left:12px;top:27px;width:122px;font-size:2.4px">Wir sind Ihr erstklassiger Partner für Brightwell 365 Consulting. Unsere Mission ist es, Unternehmen in einer digitalen Welt sicher und effizient zu machen. Wir bieten maßgeschneiderte Lösungen und kompetente Beratung, um Ihre Geräte, Daten und Prozesse zu schützen und Ihre Prozesse zu optimieren.</p>
  <div class="photo" role="img" aria-label="Foto: zwei Teammitglieder arbeiten am Laptop vor einer Weltkarte" style="left:138px;top:24px;width:97px;height:90px;background:linear-gradient(160deg,#eceae6,#d9d4cc 60%,#c9c3b9)"></div>
  <p class="t" style="left:12px;top:68px;font-size:3.4px;color:var(--ink)">Was machen wir?</p>
  <svg class="art" viewBox="0 0 235 132" font-family="Oxanium" font-size="2.2" fill="#6d7075">
    <g fill="#fff" stroke="#e3e4e8" stroke-width=".4">
      <rect x="13" y="82" width="30" height="26"/><rect x="80" y="82" width="30" height="26"/><rect x="113" y="82" width="30" height="26"/><rect x="146" y="82" width="30" height="26"/><rect x="179" y="82" width="30" height="26"/>
    </g>
    <rect x="46.5" y="82" width="31" height="26" fill="#c5d300"/>
    <text x="15" y="87">Beratung /</text><text x="15" y="90">Implementierung</text>
    <text x="49" y="87" fill="#fff">User Adoption /</text><text x="49" y="90" fill="#fff">Training</text>
    <text x="82" y="87">Tenant Review</text>
    <text x="115" y="87">Sicherheitsanalyse</text>
    <text x="148" y="87">Backup -</text><text x="148" y="90">Lösungen</text>
    <text x="181" y="87">Security</text><text x="181" y="90">Operations</text><text x="181" y="93">Center (SOC)</text>
    <g fill="none" stroke="#c5d300" stroke-width=".5"><circle cx="36" cy="102" r="2.5"/><circle cx="102" cy="102" r="2.5"/><circle cx="135" cy="102" r="2.5"/><circle cx="168" cy="102" r="2.5"/><circle cx="201" cy="102" r="2.5"/></g>
    <circle cx="70" cy="102" r="2.5" fill="none" stroke="#fff" stroke-width=".5"/>
  </svg>
  <p class="foot-brand">velora</p><p class="foot-band">Secure business and ideas in a digital world | 3</p>
</section>

<!-- 4 Statistics -->
<section class="slide" style="left:833px;top:43px">
  <h2 class="slide-title">Our Statistics</h2><p class="slide-url">www.velorasystems.de</p>
  <p class="t" style="left:28px;top:40px;width:180px;text-align:center;font-size:2.4px"><span class="hi">Lorem ipsum</span> dolor sit amet, consectetuer adipiscing elit. Maecenas porttitor congue massa. Fusce posuere, magna sed pulvinar ultricies, purus lectus malesuada libero, sit amet commodo magna eros quis urna. Nunc viverra imperdiet enim. Fusce est. Vivamus a tellus. Pellentesque habitant morbi tristique senectus et netus et malesuada fames ac turpis egestas.</p>
  <svg class="art" viewBox="0 0 235 132" font-family="Oxanium" text-anchor="middle">
    <g font-size="5.6" fill="#3c3c3c"><text x="40" y="92">41</text><text x="93" y="92">1290</text><text x="146" y="92">23</text><text x="195" y="92">14</text></g>
    <g font-size="2.6" fill="#9a9ca1"><text x="40" y="98">Total Branch</text><text x="93" y="98">Satisfy Customer</text><text x="146" y="98">Partnership</text><text x="195" y="98">Certifications</text></g>
  </svg>
  <p class="foot-brand">velora</p><p class="foot-band">Secure business and ideas in a digital world | 4</p>
</section>

<!-- 5 Hauptvorteile -->
<section class="slide" style="left:35px;top:207px">
  <h2 class="slide-title">Hauptvorteile der velora systems</h2><p class="slide-url">www.velorasystems.de</p>
  <svg class="art" viewBox="0 0 235 132" font-family="Oxanium" font-size="2.4" fill="#6d7075">
    <rect x="64" y="33" width="52" height="74" fill="#c5d300"/>
    <g fill="#c5d300"><text x="14" y="49">Listenpunkttitel Eins</text><text x="122" y="49">Listenpunkttitel Drei</text><text x="176" y="49">Listenpunkttitel Vier</text></g>
    <text x="68" y="42" fill="#fff">Listenpunkttitel Zwei</text>
    <g fill="none" stroke="#9a9ca1" stroke-width=".5"><circle cx="18" cy="40" r="2.5"/><rect x="124" y="37" width="6" height="5"/><circle cx="178" cy="40" r="2.5"/></g>
    <g fill="none" stroke="#fff" stroke-width=".5"><circle cx="71" cy="37" r="2.5"/></g>
    <g id="bul">
      <text x="17" y="56">• Dies ist nur ein</text><text x="19" y="59.5">Textbeispiel, das Sie an</text><text x="19" y="63">den Inhalt Ihrer</text><text x="19" y="66.5">Präsentation anpassen</text><text x="19" y="70">können.</text>
      <text x="17" y="76">• Dies ist nur ein</text><text x="19" y="79.5">Textbeispiel, das Sie an</text><text x="19" y="83">den Inhalt Ihrer</text><text x="19" y="86.5">Präsentation anpassen</text><text x="19" y="90">können.</text>
    </g>
    <use href="#bul" x="108"/><use href="#bul" x="162"/>
    <use href="#bul" x="54" fill="#fff" y="-5"/>
  </svg>
  <p class="foot-brand">velora</p><p class="foot-band">Secure business and ideas in a digital world | 5</p>
</section>

<!-- 6 Inhaltsfolie -->
<section class="slide" style="left:301px;top:207px">
  <h2 class="slide-title">Inhaltsfolie</h2><p class="slide-url">www.velorasystems.de</p>
  <svg class="art" viewBox="0 0 235 132" font-family="Oxanium" font-size="2.8" fill="#6d7075" text-anchor="middle">
    <g fill="#fff" stroke="#e3e4e8" stroke-width=".6">
      <polygon points="24,46 34,28 54,28 64,46 54,64 34,64"/>
      <polygon points="74,46 84,28 104,28 114,46 104,64 84,64"/>
      <polygon points="24,86 34,68 54,68 64,86 54,104 34,104"/>
      <polygon points="74,86 84,68 104,68 114,86 104,104 84,104"/>
    </g>
    <polygon points="49,66 58,50 78,50 87,66 78,82 58,82" fill="#c5d300"/>
    <text x="68" y="67.5" fill="#fff">Kernbotschaften</text>
    <g font-size="9" fill="#eceef0"><text x="44" y="45">1</text><text x="94" y="45">2</text><text x="44" y="97">3</text><text x="94" y="97">4</text></g>
    <text x="44" y="45">Punkt</text><text x="44" y="49">Nummer Eins</text>
    <text x="94" y="45">Punkt</text><text x="94" y="49">Nummer Zwei</text>
    <text x="34" y="91">Punkt</text><text x="34" y="95">Nummer Drei</text>
    <text x="94" y="91">Punkt</text><text x="94" y="95">Nummer Vier</text>
    <g text-anchor="start">
      <g id="row6"><circle cx="126" cy="26" r="3.4" fill="#c5d300"/><text x="133" y="24.5" fill="#3c3c3c" font-size="2.8">Titel des Punktabschnitts</text><text x="133" y="28.5" font-size="2.3">Dies ist nur einfacher Text. Sie können ihn an</text><text x="133" y="31.5" font-size="2.3">den Inhalt Ihrer Präsentation anpassen.</text></g>
      <use href="#row6" y="20"/><use href="#row6" y="40"/><use href="#row6" y="60"/><use href="#row6" y="80"/>
    </g>
  </svg>
  <p class="foot-brand">velora</p><p class="foot-band">Secure business and ideas in a digital world | 6</p>
</section>

<!-- 7 Table Plan Chart -->
<section class="slide" style="left:567px;top:207px">
  <h2 class="slide-title">2025 Table Plan Chart</h2><p class="slide-url">www.velorasystems.de</p>
  <svg class="art" viewBox="0 0 235 132" font-family="Oxanium">
    <text x="12" y="62" font-size="26" fill="#f3f4f6" font-weight="600">2025</text>
    <text x="147" y="22" font-size="3.6" fill="#3c3c3c">1.021+ <tspan font-size="2.6" fill="#6d7075">People</tspan></text>
    <text x="147" y="28" font-size="2.6" fill="#6d7075">Your partner for specialty fiber</text><text x="147" y="31.5" font-size="2.6" fill="#6d7075">optic</text>
    <rect x="20" y="66" width="200" height="46" fill="#fff" stroke="#e3e4e8" stroke-width=".4"/>
    <g fill="#3c3c3c">
      <rect x="32" y="80" width="3" height="26"/><rect x="47" y="78" width="3" height="28"/><rect x="62" y="81" width="3" height="25"/><rect x="77" y="79" width="3" height="27"/><rect x="92" y="77" width="3" height="29"/><rect x="107" y="80" width="3" height="26"/><rect x="122" y="78" width="3" height="28"/><rect x="137" y="80" width="3" height="26"/><rect x="152" y="81" width="3" height="25"/><rect x="167" y="76" width="3" height="30"/><rect x="182" y="77" width="3" height="29"/><rect x="197" y="74" width="3" height="32"/>
    </g>
    <g font-size="2.4" fill="#c5d300" text-anchor="middle">
      <text x="33.5" y="76">76%</text><text x="48.5" y="74">82%</text><text x="63.5" y="77">74%</text><text x="78.5" y="75">80%</text><text x="93.5" y="73">87%</text><text x="108.5" y="76">72%</text><text x="123.5" y="74">83%</text><text x="138.5" y="76">77%</text><text x="153.5" y="77">72%</text><text x="168.5" y="72">85%</text><text x="183.5" y="73">86%</text><text x="198.5" y="70">90%</text>
      <g fill="#9a9ca1"><text x="33.5" y="110">Jan</text><text x="48.5" y="110">Feb</text><text x="63.5" y="110">Mar</text><text x="78.5" y="110">Apr</text><text x="93.5" y="110">May</text><text x="108.5" y="110">Jun</text><text x="123.5" y="110">Jul</text><text x="138.5" y="110">Aug</text><text x="153.5" y="110">Sep</text><text x="168.5" y="110">Oct</text><text x="183.5" y="110">Nov</text><text x="198.5" y="110">Dec</text></g>
    </g>
  </svg>
  <p class="foot-brand">velora</p><p class="foot-band">Secure business and ideas in a digital world | 7</p>
</section>

<!-- 8 Table Plan Chart 2 -->
<section class="slide" style="left:833px;top:207px">
  <h2 class="slide-title">2025 Table Plan Chart</h2><p class="slide-url">www.velorasystems.de</p>
  <svg class="art" viewBox="0 0 235 132" font-family="Oxanium">
    <g font-size="5" fill="#3c3c3c"><text x="12" y="57">A wonderful</text><text x="12" y="63.5">effort <tspan fill="#c5d300">has</tspan></text><text x="12" y="70" fill="#c5d300">taken</text><text x="12" y="76.5" fill="#c5d300">possession</text></g>
    <text x="68" y="34" font-size="2.6" fill="#9a9ca1">Your partner for specialty fiber optic</text>
    <g stroke="#eceef0" stroke-width=".3"><line x1="72" y1="40" x2="160" y2="40"/><line x1="72" y1="54" x2="160" y2="54"/><line x1="72" y1="68" x2="160" y2="68"/><line x1="72" y1="82" x2="160" y2="82"/><line x1="72" y1="96" x2="160" y2="96"/><line x1="72" y1="108" x2="160" y2="108"/></g>
    <g fill="#c5d300"><rect x="78" y="100" width="4.5" height="8"/><rect x="92" y="92" width="4.5" height="16"/><rect x="106" y="86" width="4.5" height="22"/><rect x="120" y="77" width="4.5" height="31"/><rect x="134" y="70" width="4.5" height="38"/><rect x="148" y="48" width="4.5" height="60"/></g>
    <g font-size="2.2" fill="#9a9ca1"><text x="75" y="112">Week 1</text><text x="89" y="112">Week 2</text><text x="103" y="112">Week 3</text><text x="117" y="112">Week 4</text><text x="131" y="112">Week 5</text><text x="145" y="112">Week 6</text></g>
    <circle cx="196" cy="35" r="11" fill="none" stroke="#eceef0" stroke-width="2"/><circle cx="196" cy="35" r="11" fill="none" stroke="#c5d300" stroke-width="2" stroke-dasharray="36.6 69" transform="rotate(-90 196 35)"/>
    <circle cx="196" cy="84" r="11" fill="none" stroke="#eceef0" stroke-width="2"/><circle cx="196" cy="84" r="11" fill="none" stroke="#c5d300" stroke-width="2" stroke-dasharray="50.4 69" transform="rotate(-90 196 84)"/>
    <g text-anchor="middle"><text x="196" y="36.5" font-size="4" fill="#3c3c3c">53%</text><text x="196" y="85.5" font-size="4" fill="#3c3c3c">73%</text>
    <text x="196" y="53" font-size="3" fill="#3c3c3c">Reports</text><text x="196" y="56" font-size="2.2" fill="#c5d300">2021</text>
    <text x="196" y="102" font-size="3" fill="#3c3c3c">Reports</text><text x="196" y="105" font-size="2.2" fill="#c5d300">2021</text></g>
  </svg>
  <p class="foot-brand">velora</p><p class="foot-band">Secure business and ideas in a digital world | 8</p>
</section>

<!-- 9 Year Plan -->
<section class="slide" style="left:35px;top:370px">
  <h2 class="slide-title">Year Plan Table Chart</h2><p class="slide-url">www.velorasystems.de</p>
  <svg class="art" viewBox="0 0 235 132" font-family="Oxanium">
    <text x="4" y="66" font-size="32" fill="#f4f5f7" font-weight="600">2025</text>
    <g fill="#f0f1f3"><rect x="20" y="106" width="12" height="26"/><rect x="70" y="88" width="12" height="44"/><rect x="100" y="80" width="12" height="52"/><rect x="150" y="90" width="12" height="42"/></g>
    <rect x="52" y="76" width="13" height="56" fill="#c5d300"/><rect x="118" y="96" width="13" height="36" fill="#c5d300"/><rect x="135" y="86" width="13" height="46" fill="#6d7075"/>
    <path d="M20,120 C40,60 70,70 90,100 S120,110 150,70" fill="none" stroke="#e7ee8c" stroke-width=".6"/>
    <g font-size="3.6" fill="#3c3c3c" font-weight="600"><text x="53" y="73">2022</text><text x="117" y="93">2020</text><text x="136" y="83">2030</text></g>
    <g font-size="3" fill="#c5c7cb"><text x="20" y="103">2014</text><text x="36" y="89">2017</text><text x="69" y="85">2023</text><text x="100" y="77">2025</text><text x="150" y="87">2032</text></g>
    <polygon points="165,52 170,47 175,52 172,52 172,57 168,57 168,52" fill="#c5d300"/>
    <text x="180" y="52" font-size="4" fill="#3c3c3c">3.021+ <tspan font-size="2.6" fill="#9a9ca1">Users</tspan></text>
    <text x="180" y="58" font-size="2.6" fill="#9a9ca1">Your partner for</text><text x="180" y="61.5" font-size="2.6" fill="#9a9ca1">specialty fiber optic</text>
    <polygon points="165,82 170,87 175,82 172,82 172,77 168,77 168,82" fill="#c5d300"/>
    <text x="180" y="86" font-size="4" fill="#3c3c3c">2.021+ <tspan font-size="2.6" fill="#9a9ca1">Users</tspan></text>
    <text x="180" y="92" font-size="2.6" fill="#9a9ca1">Your partner for</text><text x="180" y="95.5" font-size="2.6" fill="#9a9ca1">specialty fiber optic</text>
  </svg>
</section>

<!-- 10 Plan Profit -->
<section class="slide" style="left:301px;top:370px">
  <h2 class="slide-title">Plan Profit Company</h2><p class="slide-url">www.velorasystems.de</p>
  <svg class="art" viewBox="0 0 235 132" font-family="Oxanium">
    <g stroke="#eceef0" stroke-width=".3"><line x1="28" y1="28" x2="210" y2="28"/><line x1="28" y1="36" x2="210" y2="36"/><line x1="28" y1="44" x2="210" y2="44"/><line x1="28" y1="52" x2="210" y2="52"/><line x1="28" y1="60" x2="210" y2="60"/><line x1="28" y1="68" x2="210" y2="68"/></g>
    <g font-size="2" fill="#9a9ca1"><text x="20" y="29">100</text><text x="22" y="37">80</text><text x="22" y="45">60</text><text x="22" y="53">40</text><text x="22" y="61">20</text><text x="23" y="69">0</text></g>
    <g fill="#e7ee8c"><rect x="33" y="61" width="3" height="7"/><rect x="48" y="63" width="3" height="5"/><rect x="63" y="58" width="3" height="10"/><rect x="78" y="59" width="3" height="9"/><rect x="93" y="60" width="3" height="8"/><rect x="108" y="62" width="3" height="6"/><rect x="123" y="59" width="3" height="9"/><rect x="138" y="58" width="3" height="10"/><rect x="153" y="56" width="3" height="12"/><rect x="168" y="55" width="3" height="13"/><rect x="183" y="50" width="3" height="18"/><rect x="198" y="46" width="3" height="22"/></g>
    <g fill="#c5d300"><rect x="36" y="62" width="3" height="6"/><rect x="51" y="60" width="3" height="8"/><rect x="66" y="57" width="3" height="11"/><rect x="81" y="60" width="3" height="8"/><rect x="96" y="61" width="3" height="7"/><rect x="111" y="58" width="3" height="10"/><rect x="126" y="55" width="3" height="13"/><rect x="141" y="60" width="3" height="8"/><rect x="156" y="52" width="3" height="16"/><rect x="171" y="53" width="3" height="15"/><rect x="186" y="48" width="3" height="20"/><rect x="201" y="44" width="3" height="24"/></g>
    <polyline points="35,58 50,61 65,52 80,56 95,47 110,54 125,40 140,56 155,40 170,44 185,36 200,32 205,30" fill="none" stroke="#3c3c3c" stroke-width=".4"/>
    <g font-size="1.9" fill="#9a9ca1" text-anchor="middle"><text x="36" y="73">January</text><text x="51" y="73">February</text><text x="66" y="73">March</text><text x="81" y="73">April</text><text x="96" y="73">May</text><text x="111" y="73">June</text><text x="126" y="73">July</text><text x="141" y="73">August</text><text x="156" y="73">September</text><text x="171" y="73">October</text><text x="186" y="73">November</text><text x="201" y="73">December</text></g>
    <text x="23" y="94" font-size="4.4" fill="#3c3c3c">A <tspan fill="#c5d300">wonderful</tspan> effort has</text>
    <text x="23" y="100" font-size="4.4" fill="#3c3c3c">taken possession</text>
    <text x="23" y="105" font-size="2.6" fill="#9a9ca1">Your partner for specialty fiber optic</text>
    <circle cx="137" cy="96" r="6" fill="#c5d300"/><circle cx="170" cy="96" r="6" fill="#fff" stroke="#e3e4e8" stroke-width=".5"/><circle cx="203" cy="96" r="6" fill="#fff" stroke="#e3e4e8" stroke-width=".5"/>
    <g font-size="3" fill="#3c3c3c" text-anchor="middle"><text x="137" y="108">Profit</text><text x="170" y="108">Small team</text><text x="203" y="108">Company</text></g>
  </svg>
  <p class="foot-brand">velora</p><p class="foot-band">Secure business and ideas in a digital world | 10</p>
</section>

<!-- 11 Incomegraphic -->
<section class="slide" style="left:567px;top:370px">
  <h2 class="slide-title">2025 Incomegraphic</h2><p class="slide-url">www.velorasystems.de</p>
  <svg class="art" viewBox="0 0 235 132" font-family="Oxanium">
    <text x="20" y="72" font-size="40" fill="#eef0f2" font-weight="600">2025</text>
  </svg>
  <div class="photo" role="img" aria-label="Illustration: gestapelte 3D-Ringe als Einkommensstufen" style="left:48px;top:42px;width:140px;height:74px;border-radius:50%;background:radial-gradient(ellipse at 50% 35%,#dbe566 0%,#c5d300 28%,#a6a9ad 52%,#7b7e83 80%,rgba(123,126,131,0) 100%)"></div>
  <svg class="art" viewBox="0 0 235 132" font-family="Oxanium">
    <g font-size="5" fill="#c5d300"><text x="138" y="46">$256,2</text><text x="50" y="60">$412,2</text></g>
    <g font-size="5" fill="#3c3c3c"><text x="22" y="82">$832,2</text><text x="168" y="66">$523,2</text></g>
    <g font-size="2.2" fill="#9a9ca1"><text x="146" y="50">Income</text><text x="72" y="60">Income</text><text x="26" y="86">Income</text><text x="175" y="70">Income</text></g>
  </svg>
  <p class="foot-brand">velora</p><p class="foot-band">Secure business and ideas in a digital world | 11</p>
</section>

<!-- 12 Incomegraphic 2 -->
<section class="slide" style="left:833px;top:370px">
  <h2 class="slide-title">2025 Incomegraphic</h2><p class="slide-url">www.velorasystems.de</p>
  <svg class="art" viewBox="0 0 235 132" font-family="Oxanium">
    <text x="117" y="30" font-size="6" fill="#3c3c3c" text-anchor="middle">A <tspan fill="#c5d300">remarkable</tspan> achievement that</text>
    <text x="117" y="37.5" font-size="6" fill="#3c3c3c" text-anchor="middle">defines the future of innovation</text>
    <text x="117" y="44" font-size="2.5" fill="#9a9ca1" text-anchor="middle">A wonderful serenity has taken like these sweet mornings of</text>
    <text x="117" y="47.5" font-size="2.5" fill="#9a9ca1" text-anchor="middle">spring which.</text>
    <g stroke="#eceef0" stroke-width=".3"><line x1="40" y1="60" x2="210" y2="60"/><line x1="40" y1="69" x2="210" y2="69"/><line x1="40" y1="78" x2="210" y2="78"/><line x1="40" y1="87" x2="210" y2="87"/><line x1="40" y1="96" x2="210" y2="96"/></g>
    <g font-size="2.3" fill="#9a9ca1"><text x="30" y="61">400</text><text x="30" y="70">300</text><text x="30" y="79">200</text><text x="30" y="88">100</text><text x="33" y="97">0</text></g>
    <path d="M46,68 C56,62 60,92 70,88 S90,75 100,80 S120,85 135,84 S150,80 158,82 S170,70 180,70 S190,76 200,68" fill="none" stroke="#c5d300" stroke-width=".7"/>
    <circle cx="78" cy="62" r="4" fill="#c5d300"/><text x="88" y="63.5" font-size="3.2" fill="#3c3c3c">Precision Company</text>
    <circle cx="148" cy="82" r="4" fill="#c5d300"/><text x="158" y="83.5" font-size="3" fill="#c5d300">Sustainable Growth</text>
    <g font-size="2.4" fill="#3c3c3c" text-anchor="middle"><text x="46" y="101">Week 1</text><text x="69" y="101">Week 2</text><text x="92" y="101">Week 3</text><text x="115" y="101">Week 4</text><text x="138" y="101">Week 1</text><text x="161" y="101">Week 2</text><text x="184" y="101">Week 3</text></g>
  </svg>
  <p class="foot-brand">velora</p><p class="foot-band">Secure business and ideas in a digital world | 12</p>
</section>

<!-- 13 Tablet Chart -->
<section class="slide" style="left:35px;top:534px">
  <h2 class="slide-title">2025 Tablet Chart</h2><p class="slide-url">www.velorasystems.de</p>
  <svg class="art" viewBox="0 0 235 132" font-family="Oxanium">
    <text x="117" y="30" font-size="6" fill="#3c3c3c" text-anchor="middle">A <tspan fill="#c5d300">powerful</tspan> legacy built on trust,</text>
    <text x="117" y="37.5" font-size="6" fill="#3c3c3c" text-anchor="middle">innovation, and leadership.</text>
    <text x="117" y="45" font-size="5.4" fill="#c5d300" text-anchor="middle">70.5%</text>
    <text x="117" y="49" font-size="2.2" fill="#9a9ca1" text-anchor="middle">Enter Point</text>
    <g stroke="#eceef0" stroke-width=".3"><line x1="25" y1="52" x2="215" y2="52"/><line x1="25" y1="62" x2="215" y2="62"/><line x1="25" y1="72" x2="215" y2="72"/><line x1="25" y1="82" x2="215" y2="82"/><line x1="25" y1="92" x2="215" y2="92"/><line x1="25" y1="106" x2="215" y2="106"/></g>
    <g fill="#e7ee8c"><rect x="30" y="99" width="3" height="7"/><rect x="46" y="100" width="3" height="6"/><rect x="62" y="96" width="3" height="10"/><rect x="78" y="97" width="3" height="9"/><rect x="94" y="98" width="3" height="8"/><rect x="110" y="99" width="3" height="7"/><rect x="126" y="94" width="3" height="12"/><rect x="142" y="96" width="3" height="10"/><rect x="158" y="90" width="3" height="16"/><rect x="174" y="86" width="3" height="20"/><rect x="190" y="80" width="3" height="26"/><rect x="206" y="74" width="3" height="32"/></g>
    <g fill="#c5d300"><rect x="33" y="98" width="3" height="8"/><rect x="49" y="97" width="3" height="9"/><rect x="65" y="94" width="3" height="12"/><rect x="81" y="96" width="3" height="10"/><rect x="97" y="92" width="3" height="14"/><rect x="113" y="96" width="3" height="10"/><rect x="129" y="90" width="3" height="16"/><rect x="145" y="95" width="3" height="11"/><rect x="161" y="86" width="3" height="20"/><rect x="177" y="84" width="3" height="22"/><rect x="193" y="78" width="3" height="28"/><rect x="209" y="72" width="3" height="34"/></g>
    <polyline points="32,92 48,96 64,82 80,86 96,76 112,90 128,74 144,95 160,78 176,80 192,70 208,64 212,62" fill="none" stroke="#3c3c3c" stroke-width=".4"/>
    <g font-size="1.9" fill="#9a9ca1" text-anchor="middle"><text x="34" y="110">January</text><text x="50" y="110">February</text><text x="66" y="110">March</text><text x="82" y="110">April</text><text x="98" y="110">May</text><text x="114" y="110">June</text><text x="130" y="110">July</text><text x="146" y="110">August</text><text x="162" y="110">September</text><text x="178" y="110">October</text><text x="194" y="110">November</text><text x="210" y="110">December</text></g>
  </svg>
  <p class="foot-brand">velora</p><p class="foot-band">Secure business and ideas in a digital world | 13</p>
</section>

<!-- 14 Wavegraphic -->
<section class="slide" style="left:301px;top:534px">
  <h2 class="slide-title">2025 Wavegraphic</h2><p class="slide-url">www.velorasystems.de</p>
  <svg class="art" viewBox="0 0 235 132" font-family="Oxanium">
    <g stroke="#eceef0" stroke-width=".3"><line x1="30" y1="25" x2="215" y2="25"/><line x1="30" y1="37" x2="215" y2="37"/><line x1="30" y1="49" x2="215" y2="49"/><line x1="30" y1="61" x2="215" y2="61"/><line x1="30" y1="73" x2="215" y2="73"/></g>
    <g font-size="2.4" fill="#9a9ca1"><text x="20" y="26">400</text><text x="20" y="38">300</text><text x="20" y="50">200</text><text x="20" y="62">100</text><text x="22" y="74">0</text></g>
    <path d="M45,68 C70,60 80,28 100,40 S120,55 130,30 S150,20 170,45 S200,60 215,45" fill="none" stroke="#c5d300" stroke-width=".8"/>
    <path d="M45,62 C65,52 75,50 95,42 S120,38 140,52 S160,70 180,48 S200,40 215,42" fill="none" stroke="#6d7075" stroke-width=".5"/>
    <path d="M45,58 C60,40 80,70 100,60 S130,40 150,55 S180,75 215,60" fill="none" stroke="#dbe566" stroke-width=".5"/>
    <path d="M76,28 l1.2,-1.2 a1,1 0 0,1 1.5,1.5 l-2.7,2.7 l-2.7,-2.7 a1,1 0 0,1 1.5,-1.5 z" fill="#e5484d"/>
    <text x="83" y="29" font-size="2.4" fill="#6d7075">Our</text><text x="83" y="32" font-size="2.4" fill="#6d7075">target</text>
    <g font-size="2.6" fill="#9a9ca1"><text x="33" y="92">Option</text><text x="75" y="92">Option</text><text x="118" y="92">Option</text></g>
    <g font-size="10"><text x="29" y="104" fill="#c5d300">50</text><text x="72" y="104" fill="#e7ee8c">67</text><text x="114" y="104" fill="#6d7075">42</text></g>
    <g font-size="3.8" fill="#3c3c3c"><text x="153" y="95">A foundation of</text><text x="153" y="100">expertise, paving the</text><text x="153" y="105">way for <tspan fill="#c5d300">future</tspan></text><text x="153" y="110" fill="#c5d300">success</text></g>
  </svg>
  <p class="foot-brand">velora</p><p class="foot-band">Secure business and ideas in a digital world | 14</p>
</section>

<!-- 15 Customer Target -->
<section class="slide" style="left:567px;top:534px">
  <h2 class="slide-title">2025 Costumer Target</h2><p class="slide-url">www.velorasystems.de</p>
  <svg class="art" viewBox="0 0 235 132" font-family="Oxanium">
    <text x="15" y="24" font-size="3.4" fill="#3c3c3c">Total <tspan fill="#c5d300">5,340</tspan> nodes found</text>
    <rect x="22" y="28" width="194" height="82" rx="3" fill="#fff" stroke="#e3e4e8" stroke-width=".5"/>
    <g font-size="3" fill="#3c3c3c"><text x="33" y="39">No.  Contries</text><text x="117" y="39">Last 24 Hours</text><text x="168" y="39">Last 7 Days</text></g>
    <g font-size="2.4" fill="#9a9ca1">
      <text x="34" y="52">1.</text><text x="62" y="52">United Kingdom</text><text x="117" y="52">2,453(31%)</text>
      <text x="34" y="63.5">2.</text><text x="62" y="63.5">Singapore</text><text x="117" y="63.5">1,233(28,5%)</text>
      <text x="34" y="75">3.</text><text x="62" y="75">Germany</text><text x="117" y="75">453(3,23%)</text>
      <text x="34" y="86.5">4.</text><text x="62" y="86.5">Swiss</text><text x="117" y="86.5">348(2,58%)</text>
      <text x="34" y="98">5.</text><text x="62" y="98">Spain</text><text x="117" y="98">100(1,47%)</text>
    </g>
    <g font-size="2.6"><text x="168" y="52" fill="#e5484d">0,53%</text><text x="168" y="63.5" fill="#e5484d">1,62%</text><text x="168" y="75" fill="#57b642">4,60%</text><text x="168" y="86.5" fill="#e5484d">0,2%</text><text x="168" y="98" fill="#57b642">6,10%</text></g>
    <g fill="#c4c6cb"><rect x="44" y="48.5" width="9" height="5"/><rect x="44" y="60" width="9" height="5"/><rect x="44" y="71.5" width="9" height="5"/><rect x="44" y="83" width="9" height="5"/><rect x="44" y="94.5" width="9" height="5"/></g>
  </svg>
  <p class="foot-brand">velora</p><p class="foot-band">Secure business and ideas in a digital world | 15</p>
</section>

<!-- 16 Q1-Q4 Report -->
<section class="slide" style="left:833px;top:534px">
  <h2 class="slide-title">2025 Table Q1-Q4 Report</h2><p class="slide-url">www.velorasystems.de</p>
  <svg class="art" viewBox="0 0 235 132" font-family="Oxanium">
    <rect x="15" y="25" width="206" height="6" fill="#3c3c3c"/>
    <g font-size="2.4" fill="#fff"><text x="18" y="29">#</text><text x="44" y="29">Title here</text><text x="92" y="29">Title here</text><text x="108" y="29">Title here</text><text x="125" y="29">Title here</text><text x="143" y="29">Value</text><text x="158" y="29">Title here</text><text x="175" y="29">Value</text></g>
    <g stroke="#eceef0" stroke-width=".3"><line x1="15" y1="41" x2="221" y2="41"/><line x1="15" y1="51" x2="221" y2="51"/><line x1="15" y1="61" x2="221" y2="61"/><line x1="15" y1="71" x2="221" y2="71"/><line x1="15" y1="81" x2="221" y2="81"/></g>
    <g font-size="2" fill="#6d7075">
      <text x="18" y="37">1</text><text x="26" y="37">Your Amazing Text Goes Here</text><text x="108" y="37">$248.558</text><text x="125" y="37">John Doe</text><text x="143" y="37">Q1-Q4</text><text x="158" y="37">07442</text>
      <text x="18" y="47">2</text><text x="26" y="47">Your Cool Text Goes Here</text><text x="108" y="47">$248.558</text><text x="125" y="47">John Doe</text><text x="143" y="47">Q1-Q4</text><text x="158" y="47">07442</text>
      <text x="18" y="57">3</text><text x="26" y="57">Your Amazing Text Goes Here</text><text x="108" y="57">$248.558</text><text x="125" y="57">John Doe</text><text x="143" y="57">Q1-Q4</text><text x="158" y="57">07442</text>
      <text x="18" y="67">4</text><text x="26" y="67">Your Cool Text Goes Here</text><text x="108" y="67">$248.558</text><text x="125" y="67">John Doe</text><text x="143" y="67">-</text><text x="158" y="67">-</text>
      <text x="18" y="77">5</text><text x="26" y="77">Your Cool Text Goes Here</text><text x="108" y="77">$248.558</text><text x="125" y="77">John Doe</text><text x="143" y="77">-</text><text x="158" y="77">-</text>
    </g>
    <g font-size="2" fill="#c5d300"><text x="175" y="37">+18%</text><text x="175" y="47">-8.17%</text><text x="175" y="57">-20%</text></g>
    <text x="20" y="95" font-size="5" fill="#3c3c3c">Your partner for</text>
    <text x="20" y="102" font-size="5" fill="#c5d300">specialty <tspan fill="#3c3c3c">fiber optic</tspan></text>
    <text x="20" y="107" font-size="2.4" fill="#9a9ca1">Your partner for specialty fiber optic</text>
    <g transform="rotate(-20 188 95)"><rect x="171" y="80" width="34" height="30" rx="7" fill="#fff" stroke="#e3e4e8" stroke-width=".6"/><text x="188" y="96" font-size="8" fill="#c5d300" text-anchor="middle">$50K</text><text x="188" y="101" font-size="2.4" fill="#6d7075" text-anchor="middle">Calculation</text></g>
  </svg>
  <p class="foot-brand">velora</p><p class="foot-band">Secure business and ideas in a digital world | 16</p>
</section>

<!-- 17 Our Statistics -->
<section class="slide" style="left:35px;top:697px">
  <h2 class="slide-title">Our Statistics</h2><p class="slide-url">www.velorasystems.de</p>
  <svg class="art" viewBox="0 0 235 132" font-family="Oxanium">
    <rect x="12" y="30" width="82" height="76" fill="#fff" style="filter:drop-shadow(0 1px 3px rgba(0,0,0,.08))"/>
    <rect x="102" y="30" width="120" height="76" fill="#fff" style="filter:drop-shadow(0 1px 3px rgba(0,0,0,.08))"/>
    <text x="22" y="37" font-size="2.8" fill="#c5d300">Circle Finding Chart</text>
    <g font-size="2.2" fill="#6d7075" text-anchor="end"><text x="40" y="51">Data Five</text><text x="40" y="60">Data Four</text><text x="40" y="69">Data Three</text><text x="40" y="78">Data Two</text><text x="40" y="87">Data One</text></g>
    <rect x="42" y="49" width="14" height="3" fill="#3c3c3c"/><rect x="42" y="58" width="18" height="3" fill="#c5d300"/><rect x="42" y="67" width="30" height="3" fill="#6d7075"/><rect x="42" y="76" width="34" height="3" fill="#c5d300"/><rect x="42" y="85" width="40" height="3" fill="#3c3c3c"/>
    <g font-size="2.2" fill="#6d7075"><text x="42" y="95">0</text><text x="59" y="95">100</text><text x="79" y="95">200</text></g>
    <g id="stat17"><polygon points="118,41 121,36 127,36 130,41 127,46 121,46" fill="#c5d300"/><text x="136" y="38" font-size="2.8" fill="#3c3c3c">Titel des Punktabschnitts</text><text x="136" y="42" font-size="2.2" fill="#6d7075">Dies ist nur einfacher Text. Sie können ihn an</text><text x="136" y="45" font-size="2.2" fill="#6d7075">den Inhalt Ihrer Präsentation anpassen.</text></g>
    <use href="#stat17" y="21"/><use href="#stat17" y="42"/>
  </svg>
  <p class="foot-brand">velora</p><p class="foot-band">Secure business and ideas in a digital world | 17</p>
</section>

<!-- 18 Table dark -->
<section class="slide dark" style="left:301px;top:697px">
  <h2 class="slide-title">Table</h2><p class="slide-url">www.velorasystems.de</p>
  <svg class="art" viewBox="0 0 235 132" font-family="Oxanium">
    <polygon points="22,26 211,26 207,33 18,33" fill="#c5d300"/>
    <g font-size="2.6" fill="#fff"><text x="26" y="31">Data Name</text><text x="72" y="31">Number</text><text x="105" y="31">Profit Rate</text><text x="138" y="31">Option</text><text x="162" y="31">Rate</text><text x="180" y="31">Performance</text></g>
    <g font-size="2.6" fill="#fff">
      <text x="26" y="43">Data One</text><text x="75" y="43">5,667</text><text x="110" y="43" font-weight="600">20.45</text><text x="140" y="43">Yes</text><text x="164" y="43">70</text><text x="185" y="43">3,566</text>
      <text x="26" y="55.5">Data Two</text><text x="75" y="55.5">6,5444</text><text x="110" y="55.5">34.5</text><text x="140" y="55.5">Yes</text><text x="164" y="55.5">67</text><text x="185" y="55.5">3,997</text>
      <text x="26" y="68">Data Three</text><text x="75" y="68">54,333</text><text x="110" y="68">56.7</text><text x="140" y="68">No</text><text x="164" y="68">77</text><text x="185" y="68">9,887</text>
      <text x="26" y="80.5">Data Four</text><text x="75" y="80.5">7,655</text><text x="110" y="80.5">6.55</text><text x="140" y="80.5">No</text><text x="164" y="80.5">89</text><text x="185" y="80.5">57,666</text>
      <text x="26" y="93">Data Five</text><text x="75" y="93">7,665</text><text x="110" y="93">90</text><text x="140" y="93">Yes</text><text x="164" y="93">90</text><text x="185" y="93">98.9</text>
      <text x="26" y="105.5">Data Six</text><text x="75" y="105.5">9,999</text><text x="110" y="105.5">69</text><text x="140" y="105.5">No</text><text x="164" y="105.5">87</text><text x="185" y="105.5">98.7</text>
    </g>
    <g stroke="#555" stroke-width=".3"><line x1="67" y1="38" x2="67" y2="108"/><line x1="100" y1="38" x2="100" y2="108"/><line x1="133" y1="38" x2="133" y2="108"/><line x1="156" y1="38" x2="156" y2="108"/><line x1="176" y1="38" x2="176" y2="108"/></g>
  </svg>
  <p class="foot-brand">velora</p><p class="foot-band">Secure business and ideas in a digital world | 18</p>
</section>

<!-- 19 Project Timeline gantt -->
<section class="slide" style="left:567px;top:697px">
  <h2 class="slide-title">2025 Project Timeline</h2><p class="slide-url">www.velorasystems.de</p>
  <svg class="art" viewBox="0 0 235 132" font-family="Oxanium">
    <g stroke="#eceef0" stroke-width=".3"><line x1="62" y1="30" x2="62" y2="104"/><line x1="79" y1="30" x2="79" y2="104"/><line x1="96" y1="30" x2="96" y2="104"/><line x1="113" y1="30" x2="113" y2="104"/><line x1="130" y1="30" x2="130" y2="104"/><line x1="147" y1="30" x2="147" y2="104"/><line x1="164" y1="30" x2="164" y2="104"/><line x1="181" y1="30" x2="181" y2="104"/><line x1="198" y1="30" x2="198" y2="104"/><line x1="215" y1="30" x2="215" y2="104"/></g>
    <g font-size="2.2" fill="#9a9ca1" text-anchor="middle"><text x="71" y="29">May</text><text x="88" y="29">Jun</text><text x="105" y="29">Jul</text><text x="122" y="29">Aug</text><text x="139" y="29">Sep</text><text x="156" y="29">Oct</text><text x="173" y="29">Nov</text><text x="190" y="29">Dec</text><text x="207" y="29">Jan</text></g>
    <g fill="#fff" style="filter:drop-shadow(0 1px 2px rgba(0,0,0,.08))"><rect x="15" y="36" width="36" height="11"/><rect x="15" y="58" width="36" height="11"/><rect x="15" y="80" width="36" height="11"/></g>
    <g fill="#c5d300"><rect x="19" y="41" width="6" height="1.4"/><rect x="19" y="85" width="6" height="1.4"/></g><rect x="19" y="63" width="6" height="1.4" fill="#3c3c3c"/>
    <g font-size="2.6" fill="#3c3c3c"><text x="28" y="42.5">Team One</text><text x="28" y="64.5">Team Two</text><text x="28" y="86.5">Team Three</text></g>
    <g font-size="2" fill="#9a9ca1"><text x="57" y="43">Op 1</text><text x="57" y="65">Op 2</text><text x="57" y="87">Op 3</text></g>
    <polygon points="73,39 102,39 100,45 71,45" fill="#c5d300"/><polygon points="129,39 212,39 210,45 127,45" fill="#6d7075"/>
    <polygon points="110,51 170,51 168,57 108,57" fill="#c5d300"/>
    <polygon points="88,63 124,63 122,69 86,69" fill="#6d7075"/><polygon points="140,63 216,63 214,69 138,69" fill="#c5d300"/>
    <polygon points="107,75 184,75 182,81 105,81" fill="#c5d300"/>
    <g font-size="2" fill="#9a9ca1" text-anchor="middle"><text x="62" y="110">20</text><text x="79" y="110">20</text><text x="96" y="110">20</text><text x="113" y="110">20</text><text x="130" y="110">20</text><text x="147" y="110">20</text><text x="164" y="110">20</text><text x="181" y="110">20</text><text x="198" y="110">20</text><text x="215" y="110">20</text></g>
  </svg>
  <p class="foot-brand">velora</p><p class="foot-band">Secure business and ideas in a digital world | 19</p>
</section>

<!-- 20 Project Timeline heatmap -->
<section class="slide" style="left:833px;top:697px">
  <h2 class="slide-title">2025 Project Timeline</h2><p class="slide-url">www.velorasystems.de</p>
  <svg class="art" viewBox="0 0 235 132" font-family="Oxanium">
    <defs><pattern id="cells" x="24" y="39" width="16.8" height="9" patternUnits="userSpaceOnUse"><rect width="14" height="4.4" fill="#dfe0e4"/></pattern></defs>
    <rect x="24" y="39" width="201.6" height="63" fill="url(#cells)"/>
    <g fill="#c5d300"><rect x="142" y="48" width="14" height="4.4"/><rect x="159" y="48" width="14" height="4.4"/><rect x="209.6" y="48" width="14" height="4.4"/><rect x="74.4" y="57" width="14" height="4.4"/><rect x="125.6" y="57" width="14" height="4.4"/><rect x="57.6" y="66" width="14" height="4.4"/><rect x="176" y="66" width="14" height="4.4"/><rect x="40.8" y="75" width="14" height="4.4"/><rect x="91.2" y="75" width="14" height="4.4"/><rect x="192.8" y="75" width="14" height="4.4"/><rect x="209.6" y="75" width="14" height="4.4"/><rect x="24" y="84" width="14" height="4.4"/><rect x="108" y="84" width="14" height="4.4"/></g>
    <g font-size="2" fill="#6d7075"><text x="10" y="42.5">Sun</text><text x="10" y="51.5">Mon</text><text x="10" y="60.5">Tue</text><text x="10" y="69.5">Wed</text><text x="10" y="78.5">Thu</text><text x="10" y="87.5">Fri</text><text x="10" y="96.5">Sat</text></g>
    <g font-size="2" fill="#6d7075" text-anchor="middle"><text x="31" y="35">Jan</text><text x="47.8" y="35">Feb</text><text x="64.6" y="35">Mar</text><text x="81.4" y="35">Apr</text><text x="98.2" y="35">May</text><text x="115" y="35">Jun</text><text x="131.8" y="35">Jul</text><text x="148.6" y="35">Aug</text><text x="165.4" y="35">Sep</text><text x="182.2" y="35">Oct</text><text x="199" y="35">Nov</text><text x="215.8" y="35">Dec</text></g>
  </svg>
  <p class="foot-brand">velora</p><p class="foot-band">Secure business and ideas in a digital world | 20</p>
</section>

<!-- 21 Flow Chart -->
<section class="slide" style="left:35px;top:861px">
  <h2 class="slide-title">Flow Chart</h2><p class="slide-url">www.velorasystems.de</p>
  <svg class="art" viewBox="0 0 235 132" font-family="Oxanium" text-anchor="middle">
    <g fill="none" stroke="#c5d300" stroke-width=".5">
      <polyline points="52,35 38,35 38,75 48,75"/><line x1="82" y1="75" x2="104" y2="75"/><polyline points="124,75 124,30 164,30"/><line x1="138" y1="75" x2="164" y2="75"/><line x1="185" y1="35" x2="185" y2="63"/><line x1="185" y1="87" x2="185" y2="101"/>
    </g>
    <rect x="52" y="28" width="30" height="12" rx="6" fill="#c5d300"/><text x="67" y="35.5" font-size="4.2" fill="#fff">Start</text>
    <rect x="48" y="69" width="34" height="12" fill="#fff" style="filter:drop-shadow(0 1px 2px rgba(0,0,0,.1))"/><text x="65" y="76" font-size="3.2" fill="#6d7075">Option text</text>
    <rect x="104" y="69" width="34" height="12" fill="#fff" style="filter:drop-shadow(0 1px 2px rgba(0,0,0,.1))"/><text x="121" y="76" font-size="3.2" fill="#6d7075">Option text</text>
    <rect x="168" y="23" width="34" height="12" fill="#c5d300"/><text x="185" y="30.5" font-size="3.2" fill="#fff">Option text</text>
    <polygon points="185,61 197,75 185,89 173,75" fill="#c5d300"/><text x="185" y="74.5" font-size="2.6" fill="#fff">Flowchart</text><text x="185" y="77.5" font-size="2.6" fill="#fff">text</text>
    <rect x="168" y="101" width="34" height="12" fill="#6d7075"/><text x="185" y="108.5" font-size="3.2" fill="#fff">End Flowchart</text>
  </svg>
  <p class="foot-brand">velora</p><p class="foot-band">Secure business and ideas in a digital world | 21</p>
</section>

<!-- 22 Comparations -->
<section class="slide" style="left:301px;top:861px">
  <h2 class="slide-title">Comparations</h2><p class="slide-url">www.velorasystems.de</p>
  <svg class="art" viewBox="0 0 235 132" font-family="Oxanium">
    <rect x="21" y="37" width="94" height="56" fill="#c5d300"/>
    <rect x="119" y="40" width="94" height="50" fill="#fff" style="filter:drop-shadow(0 2px 4px rgba(0,0,0,.08))"/>
    <circle cx="110" cy="38" r="3.4" fill="#fff"/><rect x="108.5" y="36.5" width="3" height="3" fill="#c5d300"/>
    <circle cx="210" cy="39" r="5" fill="#c5d300"/><rect x="208" y="37" width="4" height="4" fill="#fff"/>
    <text x="30" y="55" font-size="6" fill="#fff">velora systems</text>
    <g font-size="3" fill="#fff"><text x="30" y="61">✓  Far far away, behind the word</text><text x="30" y="67">✓  Far from the countries</text><text x="30" y="73">✓  Far far away, behind the word</text><text x="30" y="79">✓  Far from the countries</text></g>
    <text x="130" y="55" font-size="6" fill="#3c3c3c">Other SOLUTION</text>
    <g font-size="3" fill="#9a9ca1"><text x="130" y="61"><tspan fill="#c5d300">✓</tspan>  Far far away, behind the word</text><text x="130" y="67"><tspan fill="#c5d300">✓</tspan>  Far from the countries</text><text x="130" y="73"><tspan fill="#c5d300">✓</tspan>  Far far away, behind the word</text><text x="130" y="79"><tspan fill="#c5d300">✓</tspan>  Far from the countries</text></g>
  </svg>
  <p class="foot-brand">velora</p><p class="foot-band">Secure business and ideas in a digital world | 22</p>
</section>

<!-- 23 Project Timeline circles -->
<section class="slide" style="left:567px;top:861px">
  <h2 class="slide-title">2025 Project Timeline</h2><p class="slide-url">www.velorasystems.de</p>
  <svg class="art" viewBox="0 0 235 132" font-family="Oxanium">
    <defs>
      <g id="tl23"><text x="0" y="0" font-size="3.2" fill="#3c3c3c">Q1 2025</text><text x="0" y="4" font-size="2.4" fill="#9a9ca1">Fusce posuere, magna</text><text x="0" y="7" font-size="2.4" fill="#9a9ca1">sed pulvinar ultricies,</text><text x="0" y="10" font-size="2.4" fill="#9a9ca1">purus lectus malesuad</text></g>
    </defs>
    <line x1="14" y1="70" x2="222" y2="70" stroke="#3c3c3c" stroke-width=".4"/>
    <g fill="#c5d300"><circle cx="29" cy="70" r="6"/><circle cx="68" cy="70" r="6"/><circle cx="107" cy="70" r="6"/><circle cx="146" cy="70" r="6"/><circle cx="185" cy="70" r="6"/></g>
    <g fill="none" stroke="#fff" stroke-width=".5"><circle cx="29" cy="70" r="2"/><circle cx="68" cy="70" r="2"/><circle cx="107" cy="70" r="2"/><circle cx="146" cy="70" r="2"/><circle cx="185" cy="70" r="2"/></g>
    <g stroke="#3c3c3c" stroke-width=".3"><line x1="29" y1="76" x2="29" y2="84"/><line x1="68" y1="56" x2="68" y2="64"/><line x1="107" y1="76" x2="107" y2="84"/><line x1="146" y1="56" x2="146" y2="64"/><line x1="185" y1="76" x2="185" y2="84"/></g>
    <use href="#tl23" x="28" y="90"/><use href="#tl23" x="106" y="90"/><use href="#tl23" x="184" y="90"/>
    <use href="#tl23" x="67" y="32"/><use href="#tl23" x="145" y="32"/>
  </svg>
  <p class="foot-brand">velora</p><p class="foot-band">Secure business and ideas in a digital world | 23</p>
</section>

<!-- 24 Steps -->
<section class="slide" style="left:833px;top:861px">
  <h2 class="slide-title">Steps</h2><p class="slide-url">www.velorasystems.de</p>
  <svg class="art" viewBox="0 0 235 132" font-family="Oxanium">
    <path d="M30,78 C60,85 70,70 100,55 S140,35 165,40 S200,50 210,20" fill="none" stroke="#c5d300" stroke-width=".7"/>
    <g fill="#fff" style="filter:drop-shadow(0 1px 2px rgba(0,0,0,.12))"><circle cx="30" cy="70" r="4"/><circle cx="100" cy="52" r="4"/><circle cx="172" cy="40" r="4"/></g>
    <g fill="#c5d300"><rect x="29" y="68.5" width="2.4" height="2"/><rect x="99" y="50.5" width="2.4" height="3"/><rect x="171" y="38.5" width="2.4" height="3"/></g>
    <g font-size="14" fill="#eceef0"><text x="68" y="98">1</text><text x="130" y="84">2</text><text x="200" y="72">3</text></g>
    <g font-size="4.2" fill="#3c3c3c"><text x="26" y="94">Punkt Nummer Eins</text><text x="95" y="80">Punkt Nummer Zwei</text><text x="166" y="66">Punkt Nummer Drei</text></g>
    <g font-size="2.4" fill="#9a9ca1">
      <text x="26" y="99">Dies ist nur einfacher Text. Sie</text><text x="26" y="102">können ihn an den Inhalt Ihrer</text><text x="26" y="105">Präsentation anpassen.</text>
      <text x="95" y="85">Dies ist nur einfacher Text. Sie</text><text x="95" y="88">können ihn an den Inhalt Ihrer</text><text x="95" y="91">Präsentation anpassen.</text>
      <text x="166" y="71">Dies ist nur einfacher Text. Sie</text><text x="166" y="74">können ihn an den Inhalt</text><text x="166" y="77">Ihrer Präsentation anpassen.</text>
    </g>
  </svg>
  <p class="foot-brand">velora</p><p class="foot-band">Secure business and ideas in a digital world | 24</p>
</section>

<!-- 25 Number Report -->
<section class="slide" style="left:35px;top:1024px">
  <h2 class="slide-title">Number Report</h2><p class="slide-url">www.velorasystems.de</p>
  <svg class="art" viewBox="0 0 235 132" font-family="Oxanium">
    <text x="20" y="31" font-size="5" fill="#3c3c3c">Dies ist <tspan fill="#c5d300">nur einfacher Text.</tspan> Sie können ihn</text>
    <text x="20" y="38" font-size="5" fill="#3c3c3c">an den Inhalt Ihrer Präsentation anpassen.</text>
    <path d="M22,52 l.8,-.8 a.8,.8 0 0,1 1.1,1.1 l-1.9,1.9 l-1.9,-1.9 a.8,.8 0 0,1 1.1,-1.1 z" fill="#e5484d"/>
    <text x="27" y="54" font-size="2.6" fill="#9a9ca1">Dies ist nur einfacher Text</text>
    <polyline points="25,112 64,93 104,86 140,76 180,68" fill="none" stroke="#d8d9dc" stroke-width="1.4"/>
    <polyline points="64,93 104,86" fill="none" stroke="#c5d300" stroke-width="1.4"/>
    <polyline points="104,86 140,76 180,68" fill="none" stroke="#6d7075" stroke-width="1.4"/>
    <polygon points="206,52 200,54 202,55.5 182,68 184,70 204,57.5 205,60" fill="#6d7075"/>
    <g><polygon points="64,88 68.5,90.5 68.5,95.5 64,98 59.5,95.5 59.5,90.5" fill="#c5d300"/><polygon points="104,81 108.5,83.5 108.5,88.5 104,91 99.5,88.5 99.5,83.5" fill="#c5d300"/><polygon points="140,71 144.5,73.5 144.5,78.5 140,81 135.5,78.5 135.5,73.5" fill="#3c3c3c"/><polygon points="180,63 184.5,65.5 184.5,70.5 180,73 175.5,70.5 175.5,65.5" fill="#3c3c3c"/></g>
    <g font-size="2.6" fill="#3c3c3c" text-anchor="middle"><text x="64" y="76">Reports</text><text x="104" y="69">Reports</text><text x="140" y="59">Reports</text><text x="180" y="51">Reports</text></g>
    <g font-size="5" text-anchor="middle"><text x="64" y="82" fill="#c5d300">15000</text><text x="104" y="75" fill="#e7ee8c">35000</text><text x="140" y="65" fill="#3c3c3c">45000</text><text x="180" y="57" fill="#3c3c3c">52000</text></g>
    <text x="180" y="106" font-size="2.8" fill="#9a9ca1" text-anchor="middle">Dies ist nur einfacher</text><text x="180" y="110" font-size="2.8" fill="#9a9ca1" text-anchor="middle">Text</text>
  </svg>
  <p class="foot-brand">velora</p><p class="foot-band">Secure business and ideas in a digital world | 25</p>
</section>

<!-- 26 Conclusion columns -->
<section class="slide" style="left:301px;top:1024px">
  <h2 class="slide-title">Conclusion</h2><p class="slide-url">www.velorasystems.de</p>
  <svg class="art" viewBox="0 0 235 132" font-family="Oxanium">
    <polygon points="28,22 99,22 97,28 26,28" fill="#c5d300"/><polygon points="137,22 208,22 206,28 135,28" fill="#6d7075"/>
    <g font-size="3" fill="#fff" text-anchor="middle"><text x="62" y="26.2">Titel des Punktabschnitts</text><text x="171" y="26.2">Titel des Punktabschnitts</text></g>
    <line x1="118" y1="22" x2="118" y2="112" stroke="#e3e4e8" stroke-width=".4"/>
    <g id="cc26" font-size="2.3" fill="#6d7075"><text x="23" y="38">Dies ist nur einfacher Text. Sie können ihn</text><text x="23" y="41.5">an den Inhalt Ihrer Präsentation anpassen.</text><line x1="23" y1="44.5" x2="100" y2="44.5" stroke="#e3e4e8" stroke-width=".3"/></g>
    <use href="#cc26" y="16"/><use href="#cc26" y="32"/><use href="#cc26" y="48"/><use href="#cc26" y="64"/>
    <use href="#cc26" x="107"/><use href="#cc26" x="107" y="16"/><use href="#cc26" x="107" y="32"/><use href="#cc26" x="107" y="48"/><use href="#cc26" x="107" y="64"/>
  </svg>
  <p class="foot-brand">velora</p><p class="foot-band">Secure business and ideas in a digital world | 26</p>
</section>

<!-- 27 Conclusion photo -->
<section class="slide" style="left:567px;top:1024px">
  <h2 class="slide-title">Conclusion</h2><p class="slide-url">www.velorasystems.de</p>
  <p class="t" style="left:11px;top:21px;font-size:2.8px">Lorem ipsum dolor sit amet, consectetuer adipiscing elit.</p>
  <div class="photo" role="img" aria-label="Foto: Team sitzt gemeinsam am Laptop" style="left:12px;top:36px;width:94px;height:76px;background:linear-gradient(150deg,#d6cbbd,#b59e86 50%,#8d7a68)"></div>
  <svg class="art" viewBox="0 0 235 132" font-family="Oxanium">
    <g id="row27"><rect x="116" y="36" width="9" height="7" fill="#fff" stroke="#e3e4e8" stroke-width=".4"/><circle cx="120.5" cy="39.5" r="2" fill="#c5d300"/><text x="134" y="37.5" font-size="2.8" fill="#3c3c3c">Titel des Punktabschnitts</text><text x="134" y="41.5" font-size="2.2" fill="#6d7075">Dies ist nur einfacher Text. Sie können ihn an</text><text x="134" y="44.5" font-size="2.2" fill="#6d7075">den Inhalt Ihrer Präsentation anpassen.</text></g>
    <use href="#row27" y="21.5"/><use href="#row27" y="43"/><use href="#row27" y="64.5"/>
  </svg>
  <p class="foot-brand">velora</p><p class="foot-band">Secure business and ideas in a digital world | 27</p>
</section>

<!-- 28 Icons -->
<section class="slide" style="left:833px;top:1024px">
  <h2 class="slide-title">Icon</h2><p class="slide-url">www.velorasystems.de</p>
  <svg class="art" viewBox="0 0 235 132" fill="none" stroke="#8a8c91" stroke-width=".45">
    <defs>
      <g id="ic-a"><circle cx="0" cy="0" r="3"/><circle cx="0" cy="0" r="1.2"/></g>
      <g id="ic-b"><circle cx="0" cy="-1.8" r="1.6"/><path d="M-3,3 a3,3 0 0,1 6,0"/></g>
      <g id="ic-c"><rect x="-3.5" y="-2.8" width="7" height="5"/><line x1="-1.5" y1="3.4" x2="1.5" y2="3.4"/></g>
      <g id="ic-d"><rect x="-3.5" y="-2.5" width="7" height="5"/><polyline points="-3.5,-2.5 0,0.5 3.5,-2.5"/></g>
    </defs>
    <use href="#ic-a" x="25" y="35"/><use href="#ic-b" x="62" y="35"/><use href="#ic-b" x="99" y="35"/><use href="#ic-c" x="136" y="35"/><use href="#ic-c" x="173" y="35"/><use href="#ic-c" x="210" y="35"/>
    <use href="#ic-a" x="25" y="57"/><use href="#ic-b" x="62" y="57"/><use href="#ic-b" x="99" y="57"/><use href="#ic-d" x="136" y="57"/><use href="#ic-c" x="173" y="57"/><use href="#ic-a" x="210" y="57"/>
    <use href="#ic-a" x="25" y="79"/><use href="#ic-c" x="62" y="79"/><use href="#ic-c" x="99" y="79"/><use href="#ic-a" x="136" y="79"/><use href="#ic-a" x="173" y="79"/><use href="#ic-b" x="210" y="79"/>
    <use href="#ic-b" x="25" y="101"/><use href="#ic-a" x="62" y="101"/><use href="#ic-c" x="99" y="101"/><use href="#ic-a" x="136" y="101"/><use href="#ic-b" x="173" y="101"/><use href="#ic-c" x="210" y="101"/>
  </svg>
  <p class="foot-brand">velora</p><p class="foot-band">Secure business and ideas in a digital world | 28</p>
</section>

</main>
</body>
</html>
```